Pelmora needs stationery design

We need desings for presentation cards and letter head for our company. It would be better that the letterhead uses our logo with white background and the presentation card the logo with the black background for the back of the card and the text (name, phone
Updates

Necesitas un par de días antes de escoger al ganador

Colors
0455a3
ec1f27
000000

Requirements
Must have
• Use company logo and colors

```html
<!DOCTYPE html>
<html lang="en">
<head>
<meta charset="utf-8">
<title>Pelmora Business Card</title>
<link href="https://fonts.googleapis.com/css2?family=Open+Sans:wght@400;600;700&display=swap" rel="stylesheet">
<style>
  :root {
    --brand-blue: #0455a3;
    --brand-red: #ec1f27;
    --card-black: #1a1b1d;
    --ink-white: #f4f4f4;
    --band-white: #f1f1f1;
    --band-grey: #d9d9d9;
    --backdrop: #3a3c3f;
  }
  * { box-sizing: border-box; margin: 0; padding: 0; }
  html, body {
    width: 1200px; height: 1000px; overflow: hidden;
    background: var(--backdrop);
    font-family: "Open Sans", Arial, sans-serif;
  }
  .stage {
    position: relative; width: 1200px; height: 1000px;
    display: flex; flex-direction: column; align-items: center; justify-content: center; gap: 60px;
  }
  .card {
    position: relative; width: 700px; height: 400px;
    background: var(--card-black);
    box-shadow: 0 12px 30px rgba(0,0,0,0.45);
    overflow: hidden;
  }
  .wordmark {
    color: var(--ink-white); font-weight: 600; letter-spacing: 6px;
    text-transform: uppercase; line-height: 1;
  }
  .card-back { display: flex; align-items: center; justify-content: center; }
  .card-back .wordmark { font-size: 64px; }

  .card-front .wordmark {
    position: absolute; top: 66px; right: 48px; font-size: 40px; letter-spacing: 4px;
  }
  .contact-block { position: absolute; top: 58px; left: 44px; }
  .person-name { color: var(--brand-blue); font-weight: 700; font-size: 22px; line-height: 1.1; text-transform: uppercase; }
  .person-role { color: var(--brand-red); font-size: 16px; text-transform: uppercase; margin-bottom: 12px; }
  .contact-list { list-style: none; }
  .contact-list li {
    display: flex; align-items: center; gap: 12px;
    color: var(--ink-white); font-size: 17px; line-height: 26px;
  }
  .contact-list svg { width: 16px; height: 16px; fill: var(--brand-blue); flex: none; }

  .address-band {
    position: absolute; left: 0; right: 0; bottom: 34px; height: 52px; display: flex;
  }
  .address-strip {
    background: var(--band-white); width: 440px; display: flex; align-items: center;
    padding-left: 40px; font-size: 18px; color: #111;
  }
  .band-marker { width: 52px; background: var(--card-black); display: flex; align-items: center; justify-content: center; }
  .band-marker span { width: 26px; height: 26px; background: var(--brand-blue); }
  .grey-strip { flex: 1; background: linear-gradient(90deg, var(--band-grey), var(--band-white)); }
</style>
</head>
<body>
<main class="stage">
  <section class="card card-back">
    <div class="wordmark">Pelmora</div>
  </section>

  <section class="card card-front">
    <div class="contact-block">
      <div class="person-name">Marco Ruiz</div>
      <div class="person-role">President</div>
      <ul class="contact-list">
        <li><svg viewBox="0 0 16 16"><path d="M3 1l3 3-2 2c1 2 3 4 5 5l2-2 3 3-2 3C6 15 1 10 1 3z"/></svg>555 0142 7781</li>
        <li><svg viewBox="0 0 16 16"><path d="M4 0h8v16H4zM5.5 2v10h5V2z"/></svg>555 0198 3346</li>
        <li><svg viewBox="0 0 16 16"><path d="M4 1h8v4H4zM1 6h14v7h-3v2H4v-2H1zM5 10v4h6v-4z"/></svg>555 0127 6609</li>
        <li><svg viewBox="0 0 16 16"><path d="M1 3h14v10H1zM2 4l6 5 6-5z" fill-rule="evenodd"/></svg>marco@pelmora.com</li>
        <li><svg viewBox="0 0 16 16"><circle cx="8" cy="8" r="7"/></svg>www.pelmora.com</li>
      </ul>
    </div>
    <div class="wordmark">Pelmora</div>
    <div class="address-band">
      <div class="address-strip">2170 Harbor Lane Cedar Grove, NY 11020</div>
      <div class="band-marker"><span></span></div>
      <div class="grey-strip"></div>
    </div>
  </section>
</main>
</body>
</html>
```